Private Optometric Practice Needs new Presentation Folders/Stationary

We recently moved our office and are looking to refresh our presentation folders and stationary. I tend to prefer simple, clean designs. We are a full scope optometric practice provide high quality eyewear, custom contact lenses, along with emergency care and treatment for dry eyes. We communicate with a lot of other doctors and want to exude professionalism. I have attached 2 versions of our logo.

Target Market(s)

Familys

Industry/Entity Type

Eyecare

Font styles to use
Sans Serif

Colors
0054AA
0677BA
7BADD7
CADEEF
E8F1F8

Requirements
Nice to have
• Bifold, areas to put information about practice, welcome letter

```html
<!DOCTYPE html>
<html lang="en">
<head>
<meta charset="utf-8">
<title>Clearview Eyecare – Stationery Set</title>
<link rel="stylesheet" href="https://fonts.googleapis.com/css2?family=Montserrat:wght@400;500;600;700&display=swap">
<style>
  :root {
    --backdrop: #e3e5e9;
    --blue-deep: #0a2db4;
    --blue-royal: #0f47c8;
    --blue-brand: #0054aa;
    --blue-mid: #1a72d4;
    --blue-sky: #1d8fdc;
    --cyan: #5ad6f4;
    --pocket: #0c55b9;
    --flap: #1352c2;
    --tint: #7badd7;
    --mist: #cadeef;
    --paper: #f6f7f9;
    --paper-shade: #eaeef3;
    --ink: #3a3f46;
    --ink-soft: #6b7079;
    --white: #ffffff;
  }
  * { box-sizing: border-box; margin: 0; padding: 0; }
  html, body { width: 850px; height: 1200px; overflow: hidden; background: var(--backdrop); }
  body { font-family: "Montserrat", sans-serif; color: var(--ink); }

  .canvas { position: relative; width: 850px; height: 1200px; overflow: hidden; background: var(--backdrop); }

  /* brand name block */
  .brand { display: flex; align-items: center; gap: 0.55em; white-space: nowrap; }
  .brand-dot { width: 1em; height: 1em; border-radius: 50%; background: currentColor; flex: none; }
  .brand-name { font-weight: 400; letter-spacing: 0.22em; text-transform: uppercase; }

  /* presentation folder */
  .folder { position: absolute; left: 40px; top: 165px; width: 520px; height: 360px; filter: drop-shadow(0 6px 10px rgba(20,40,90,.18)); }
  .folder-panel { position: absolute; top: 0; width: 260px; height: 100%; }
  .folder-panel--left { left: 0; background: linear-gradient(105deg, var(--blue-deep) 0%, var(--blue-royal) 55%, var(--blue-mid) 100%); }
  .folder-panel--right { left: 260px; background: linear-gradient(215deg, var(--cyan) 0%, var(--blue-sky) 30%, var(--blue-mid) 70%, var(--blue-royal) 100%); }
  .folder-spine { position: absolute; left: 259px; top: 0; width: 2px; height: 100%; background: rgba(0,20,80,.18); }
  .pocket { position: absolute; bottom: 0; height: 118px; background: var(--pocket); }
  .pocket--left { left: 0; width: 250px; clip-path: polygon(0 0, 93% 0, 95% 4%, 100% 100%, 0 100%); }
  .pocket--right { left: 272px; width: 248px; clip-path: polygon(5% 4%, 7% 0, 100% 0, 100% 100%, 0 100%); }
  .pocket-brand { position: absolute; right: 18px; bottom: 26px; color: var(--white); font-size: 11px; }

  /* letter sheets */
  .letter { position: absolute; background: linear-gradient(160deg, var(--white) 0%, var(--paper) 55%, var(--paper-shade) 100%); overflow: hidden; }
  .letter-texture { position: absolute; right: 0; top: 0; width: 55%; height: 100%; background: radial-gradient(ellipse at 100% 10%, rgba(202,222,239,.55) 0%, rgba(232,241,248,0) 65%); }
  .letter-brand { position: absolute; left: 20px; top: 34px; font-size: 6.4px; color: var(--ink); }
  .letter-brand .brand-dot { color: var(--blue-sky); background: var(--blue-sky); width: 1.6em; height: 1.6em; }
  .letter-salutation { position: absolute; left: 20px; top: 94px; font-size: 10px; font-weight: 500; color: var(--blue-sky); }
  .letter-body { position: absolute; left: 20px; right: 18px; top: 112px; font-size: 4.3px; line-height: 1.5; color: var(--ink-soft); }
  .letter-body p + p { margin-top: 5px; }
  .letter--insert { left: 287px; top: 10px; width: 222px; height: 340px; }
  .letter--sheet { left: 590px; top: 185px; width: 220px; height: 311px; box-shadow: 0 4px 10px rgba(20,40,90,.14); }
  .letter-footer { position: absolute; left: 20px; bottom: 28px; font-size: 3.6px; line-height: 1.5; color: var(--ink-soft); text-transform: uppercase; }
  .letter-footer .footer-strong { font-size: 4.3px; font-weight: 600; color: var(--ink); letter-spacing: .02em; }
  .letter-date { position: absolute; right: 18px; bottom: 30px; font-size: 5.6px; color: var(--blue-sky); }

  /* envelopes */
  .envelope { position: absolute; top: 575px; width: 370px; height: 185px; overflow: hidden; box-shadow: 0 4px 10px rgba(20,40,90,.18); }
  .envelope--front { left: 40px; background: linear-gradient(210deg, var(--cyan) 0%, var(--blue-sky) 30%, var(--blue-royal) 75%, var(--blue-deep) 100%); }
  .envelope--front .brand { position: absolute; left: 50%; top: 50%; transform: translate(-50%, -50%); color: #3f9be8; font-size: 13px; }
  .envelope--back { left: 440px; background: linear-gradient(200deg, var(--cyan) 0%, var(--blue-sky) 25%, var(--blue-royal) 70%, var(--blue-deep) 100%); }
  .envelope-flap { position: absolute; left: 0; top: 0; width: 100%; height: 56px; }
  .envelope-address { position: absolute; left: 22px; top: 68px; color: var(--white); }
  .envelope-address .contact-name { font-size: 7.6px; font-weight: 600; letter-spacing: .03em; }
  .envelope-address .contact-lines { margin-top: 8px; font-size: 5.2px; line-height: 1.45; text-transform: uppercase; color: rgba(255,255,255,.85); }
  .envelope-address .contact-links { margin-top: 13px; font-size: 5.2px; line-height: 1.7; color: rgba(255,255,255,.85); }

  /* business cards */
  .card { position: absolute; top: 810px; width: 370px; height: 210px; overflow: hidden; box-shadow: 0 4px 10px rgba(20,40,90,.16); }
  .card--front { left: 40px; background: linear-gradient(215deg, var(--cyan) 0%, var(--blue-sky) 30%, var(--blue-royal) 72%, var(--blue-deep) 100%); }
  .card--front .brand { position: absolute; left: 50%; top: 50%; transform: translate(-50%, -50%); color: var(--white); font-size: 14px; }
  .card-texture { position: absolute; inset: 0; background: radial-gradient(ellipse at 95% 90%, rgba(123,173,215,.25) 0%, rgba(123,173,215,0) 45%), radial-gradient(ellipse at 10% 5%, rgba(123,173,215,.18) 0%, rgba(123,173,215,0) 40%); }
  .card--back { left: 440px; background: var(--white); }
  .card--back .card-texture { background: radial-gradient(ellipse at 100% 100%, rgba(202,222,239,.7) 0%, rgba(232,241,248,0) 40%), radial-gradient(ellipse at 0% 0%, rgba(202,222,239,.6) 0%, rgba(232,241,248,0) 35%); }
  .card--back .brand { position: absolute; right: 22px; top: 24px; font-size: 6.4px; color: var(--ink); }
  .card--back .brand-dot { background: var(--blue-sky); width: 1.8em; height: 1.8em; }
  .card-contact { position: absolute; left: 30px; top: 80px; }
  .card-contact .contact-name { font-size: 9px; font-weight: 600; color: var(--blue-sky); letter-spacing: .03em; text-transform: uppercase; }
  .card-contact .contact-rule { width: 120px; height: 1px; background: var(--ink-soft); margin: 6px 0 7px; }
  .card-contact .contact-lines { font-size: 6px; line-height: 1.45; text-transform: uppercase; color: var(--ink-soft); }
  .card-contact .contact-links { margin-top: 14px; font-size: 6px; line-height: 1.75; color: var(--ink-soft); }

  .contact-link { display: flex; align-items: center; gap: 4px; }
  .contact-icon { width: 1.2em; height: 1.2em; flex: none; }
  .card-contact .contact-icon { color: var(--blue-sky); }
  .envelope-address .contact-icon { color: var(--white); }
</style>
</head>
<body>
<main class="canvas">

  <!-- Presentation folder, opened -->
  <section class="folder" aria-label="Presentation folder, inside spread">
    <div class="folder-panel folder-panel--left"></div>
    <div class="folder-panel folder-panel--right"></div>
    <div class="folder-spine"></div>

    <article class="letter letter--insert">
      <div class="letter-texture" role="img" aria-label="Faint fine-line wave pattern on the letter background"></div>
      <div class="brand letter-brand"><span class="brand-dot"></span><span class="brand-name">Clearview Eyecare</span></div>
      <h2 class="letter-salutation">Your Name Here</h2>
      <div class="letter-body">
        <p>Thank you for choosing our practice for your family's eye care. We offer complete eye exams, quality eyewear, custom contact lenses, urgent visits and dry eye treatment in our new office. Our team works closely with your other doctors so every visit is calm, clear and well coordinated.</p>
        <p>Please bring your current glasses, contact lens boxes and a list of any medicines to your first visit. If you have questions before then, our front desk is happy to help by phone or through our website.</p>
        <p>We look forward to caring for your vision for many years to come. Warm regards from all of us.</p>
      </div>
    </article>

    <div class="pocket pocket--left"></div>
    <div class="pocket pocket--right">
      <div class="brand pocket-brand"><span class="brand-dot"></span><span class="brand-name">Clearview Eyecare</span></div>
    </div>
  </section>

  <!-- Letterhead -->
  <article class="letter letter--sheet" aria-label="Letterhead">
    <div class="letter-texture" role="img" aria-label="Faint fine-line wave pattern on the letter background"></div>
    <div class="brand letter-brand"><span class="brand-dot"></span><span class="brand-name">Clearview Eyecare</span></div>
    <h2 class="letter-salutation">Your Name Here</h2>
    <div class="letter-body">
      <p>Thank you for choosing our practice for your family's eye care. We offer complete eye exams, quality eyewear, custom contact lenses, urgent visits and dry eye treatment in our new office. Our team works closely with your other doctors so every visit is calm, clear and well coordinated.</p>
      <p>Please bring your current glasses, contact lens boxes and a list of any medicines to your first visit. If you have questions before then, our front desk is happy to help by phone or through our website.</p>
      <p>We look forward to caring for your vision for many years to come. Warm regards from all of us.</p>
    </div>
    <div class="letter-footer">
      4120 Lakeside Ave.<br>Suite B<br>Fairmont, MI 48210<br>
      <span class="footer-strong">+248-555-0142</span><br>
      <span class="footer-strong">www.clearvieweyecare.com</span>
    </div>
    <div class="letter-date">14/06/2024</div>
  </article>

  <!-- Envelope, front -->
  <section class="envelope envelope--front" aria-label="Envelope front">
    <div class="brand"><span class="brand-dot"></span><span class="brand-name">Clearview Eyecare</span></div>
  </section>

  <!-- Envelope, back -->
  <section class="envelope envelope--back" aria-label="Envelope back">
    <svg class="envelope-flap" viewBox="0 0 370 56" preserveAspectRatio="none" aria-hidden="true">
      <path d="M0 0 H370 V40 Q370 52 355 52 H15 Q0 52 0 40 Z" fill="#1352c2"/>
    </svg>
    <div class="envelope-address">
      <div class="contact-name">DANIEL WHITFIELD, O.D.</div>
      <div class="contact-lines">4120 Lakeside Ave.<br>Suite B<br>Fairmont, MI 48210</div>
      <div class="contact-links">
        <div class="contact-link">
          <svg class="contact-icon" viewBox="0 0 12 12" aria-hidden="true"><path d="M3 1.2 L4.6 3.4 L3.7 4.5 Q4.6 6.6 7.5 8.3 L8.6 7.4 L10.8 9 L9.8 10.6 Q5.5 10.4 1.4 4.5 Q1.2 2.6 3 1.2 Z" fill="currentColor"/></svg>
          <span>248-555-0142</span>
        </div>
        <div class="contact-link">
          <svg class="contact-icon" viewBox="0 0 12 12" aria-hidden="true"><circle cx="6" cy="6" r="4.8" fill="none" stroke="currentColor" stroke-width="1"/><ellipse cx="6" cy="6" rx="2" ry="4.8" fill="none" stroke="currentColor" stroke-width="0.9"/><path d="M1.2 6 H10.8" stroke="currentColor" stroke-width="0.9"/></svg>
          <span>WWW.CLEARVIEWEYECARE.COM</span>
        </div>
      </div>
    </div>
  </section>

  <!-- Business card, front -->
  <section class="card card--front" aria-label="Business card front">
    <div class="card-texture" role="img" aria-label="Faint polygon line pattern in light blue"></div>
    <div class="brand"><span class="brand-dot"></span><span class="brand-name">Clearview Eyecare</span></div>
  </section>

  <!-- Business card, back -->
  <section class="card card--back" aria-label="Business card back">
    <div class="card-texture" role="img" aria-label="Faint polygon line pattern in pale blue at the corners"></div>
    <div class="brand"><span class="brand-dot"></span><span class="brand-name">Clearview Eyecare</span></div>
    <div class="card-contact">
      <div class="contact-name">Daniel Whitfield, O.D.</div>
      <div class="contact-rule"></div>
      <div class="contact-lines">4120 Lakeside Ave.<br>Suite B<br>Fairmont, MI 48210</div>
      <div class="contact-links">
        <div class="contact-link">
          <svg class="contact-icon" viewBox="0 0 12 12" aria-hidden="true"><path d="M3 1.2 L4.6 3.4 L3.7 4.5 Q4.6 6.6 7.5 8.3 L8.6 7.4 L10.8 9 L9.8 10.6 Q5.5 10.4 1.4 4.5 Q1.2 2.6 3 1.2 Z" fill="currentColor"/></svg>
          <span>248-555-0142</span>
        </div>
        <div class="contact-link">
          <svg class="contact-icon" viewBox="0 0 12 12" aria-hidden="true"><circle cx="6" cy="6" r="4.8" fill="none" stroke="currentColor" stroke-width="1"/><ellipse cx="6" cy="6" rx="2" ry="4.8" fill="none" stroke="currentColor" stroke-width="0.9"/><path d="M1.2 6 H10.8" stroke="currentColor" stroke-width="0.9"/></svg>
          <span>WWW.CLEARVIEWEYECARE.COM</span>
        </div>
      </div>
    </div>
  </section>

</main>
</body>
</html>
```